Marine Business Card

We install Lighting, Sound, Video, PA Systems to hotels, nightclubs, Restaurants, Cruise Ships.

Target Market(s)

We want to focus on the Marine or Maritime/Cruise industry. Passenger ships and cruise liners are the companies we want to appeal to

Industry/Entity Type

Business

Contact Information for Business Card

Corwen Ashdale
Managing Director
Harbourne Vista Audio Marine Ltd

Requirements
Must have
• Office: 01632 960482
Mobile: 07700 900317
corwen@harbournevistaaudio.co.uk
www.harbournevistaaudio.co.uk

```html
<!DOCTYPE html>
<html lang="en">
<head>
<meta charset="utf-8">
<title>Harbourne Vista Audio Marine – Business Card</title>
<link rel="stylesheet" href="https://fonts.googleapis.com/css2?family=Lato:wght@400;700&display=swap">
<style>
  :root {
    --backdrop-light: #eeeeee;
    --backdrop-dark: #9a9a9a;
    --navy: #06232f;
    --navy-deep: #041c27;
    --ocean: #22a2dd;
    --ocean-deep: #1b95d4;
    --foam: #7ccdf3;
    --ink-light: #ffffff;
    --ink-soft: #e3f4fc;
  }
  * { margin: 0; padding: 0; box-sizing: border-box; }
  html, body {
    width: 1200px;
    height: 787px;
    overflow: hidden;
  }
  body {
    background: radial-gradient(ellipse at 50% 45%, var(--backdrop-light) 0%, #cfcfcf 55%, var(--backdrop-dark) 100%);
    font-family: "Lato", sans-serif;
    position: relative;
  }
  .card {
    position: absolute;
    top: 248px;
    width: 500px;
    height: 290px;
    overflow: hidden;
    box-shadow: 0 6px 18px rgba(0, 0, 0, 0.25);
  }
  .card-front {
    left: 70px;
    background: radial-gradient(ellipse at 50% 40%, #0a2c3b 0%, var(--navy) 60%, var(--navy-deep) 100%);
  }
  .card-back {
    left: 630px;
    background: var(--ocean);
  }
  .card-waves {
    position: absolute;
    inset: 0;
    width: 100%;
    height: 100%;
  }
  .emblem {
    position: absolute;
    left: 50%;
    top: 92px;
    width: 64px;
    height: 64px;
    margin-left: -32px;
    background: var(--ink-light);
    border-radius: 6px;
  }
  .contact-block {
    position: absolute;
    left: 150px;
    top: 126px;
    color: var(--ink-light);
  }
  .contact-name {
    font-size: 34px;
    font-weight: 700;
    letter-spacing: 0.5px;
    line-height: 1.1;
  }
  .contact-role,
  .contact-company {
    font-size: 12px;
    line-height: 1.4;
    color: var(--ink-soft);
  }
  .contact-role { margin-top: 4px; }
  .contact-lines {
    list-style: none;
    margin-top: 10px;
    font-size: 11.5px;
    line-height: 1.45;
    color: var(--ink-soft);
  }
  .contact-lines span {
    display: inline-block;
    width: 48px;
    font-weight: 700;
  }
</style>
</head>
<body>

  <section class="card card-front" aria-label="Business card front">
    <div class="emblem" role="img" aria-label="Company emblem"></div>
    <svg class="card-waves" viewBox="0 0 500 290" preserveAspectRatio="none" aria-hidden="true">
      <path d="M0 252 C90 226 160 262 250 246 S420 212 500 222 V290 H0Z" fill="var(--ocean-deep)"/>
      <path d="M0 262 C95 236 165 268 255 254 S420 228 500 236 V290 H0Z" fill="var(--foam)"/>
      <path d="M0 276 C100 262 175 284 265 272 S420 250 500 256 V290 H0Z" fill="var(--ocean-deep)"/>
    </svg>
  </section>

  <section class="card card-back" aria-label="Business card back">
    <svg class="card-waves" viewBox="0 0 500 290" preserveAspectRatio="none" aria-hidden="true">
      <path d="M0 0 H500 V48 C440 56 400 92 320 96 S150 112 0 140 Z" fill="var(--foam)"/>
      <path d="M0 0 H500 V30 C440 40 400 78 320 82 S150 98 0 124 Z" fill="var(--ocean-deep)"/>
      <path d="M0 0 H500 V18 C440 28 400 64 320 70 S150 84 0 110 Z" fill="var(--navy)"/>
    </svg>
    <div class="contact-block">
      <h1 class="contact-name">Corwen Ashdale</h1>
      <p class="contact-role">Managing Director</p>
      <p class="contact-company">Harbourne Vista Audio Marine Ltd</p>
      <ul class="contact-lines">
        <li><span>Office</span>01632 960482</li>
        <li><span>Mobile</span>07700 900317</li>
        <li>corwen@harbournevistaaudio.co.uk</li>
        <li>www.harbournevistaaudio.co.uk</li>
      </ul>
    </div>
  </section>

</body>
</html>
```